Einladungskarten Design
Zielgruppe
Die Zielgruppe besteht aus allen Privatpersonen, die eine Feier planen und auf der Suche nach individuellen, professionell gestalteten Einladungskarten für Ihre Feier sind:
Hochzeit
Geburtstag (meistens runde Geburtstage)
Mottoparty´s
Danksagung zur Gebur
Aufgabenstellung
Für das Online-Angebot www.kartenfreude-atelier.de werden kreative Vorschläge für Einladungskarten und Danksagungskarten in verschiedenen Kategorien gesucht: Hochzeit, Geburtstag, Party, Mottoparty, Geburt und weitere Themen. Das Thema ist wählbar, da für alle Kategorien neue, frische Entwürfe benötigt werden.
Dies ist kein Wettbewerb im herkömmlichen Sinne, da es keinen einzelnen Gewinner gibt. Jeder Kartenentwurf, der für das Online Angebot ausgewählt wird, wird mit 100,00 Eur honoriert.
Voraussetzung für die Honorarzahlung ist das Einverständnis der Veröffentlichung und die Übertragung der Nutzungsrechte.

```html
<!DOCTYPE html>
<html lang="de">
<head>
<meta charset="utf-8">
<title>Einladung zum 50. Geburtstag</title>
<link rel="stylesheet" href="https://fonts.googleapis.com/css2?family=Kalam:wght@300;400&family=PT+Sans+Narrow&display=swap">
<style>
  :root {
    --wine: #9c141c;
    --wine-soft: #c2434a;
    --blush: #ecd3cb;
    --paper: #ffffff;
    --backdrop: #f2f0ee;
  }
  * { box-sizing: border-box; margin: 0; padding: 0; }
  html, body { width: 1200px; height: 1200px; overflow: hidden; }
  body { background: var(--backdrop); position: relative; font-family: "PT Sans Narrow", "Arial Narrow", sans-serif; }

  .card { position: absolute; background: var(--paper); overflow: hidden; }

  /* shared band + rule system */
  .band { position: absolute; left: 0; right: 0; background: var(--wine); }
  .rule { position: absolute; left: 0; right: 0; height: 2px; background: var(--wine); }
  .band .rule-inset { position: absolute; left: 0; right: 0; height: 2px; background: var(--paper); }

  /* front cover */
  .cover { left: 420px; top: 50px; width: 360px; height: 480px; }
  .cover .band-top { top: 0; height: 24px; }
  .cover .rule-top { top: 32px; }
  .cover .band-bottom { bottom: 0; height: 74px; }
  .cover .band-bottom .rule-inset { top: 8px; }
  .cover .rule-bottom { bottom: 92px; }
  .cover .flourish {
    position: absolute; left: 210px; top: 120px; width: 200px; height: 240px;
    border-radius: 50% 10% 40% 60%;
    background: radial-gradient(ellipse at 40% 45%, var(--wine) 0%, var(--wine-soft) 45%, var(--blush) 75%, rgba(236,211,203,0) 100%);
  }
  .cover .title {
    position: absolute; left: 116px; top: 298px;
    font-family: "Kalam", cursive; font-weight: 300; font-size: 34px;
    color: var(--wine); letter-spacing: 1px;
  }

  /* inside spread */
  .inside { left: 100px; top: 590px; width: 1000px; height: 560px; }
  .inside .band-top { top: 0; height: 10px; }
  .inside .rule-top { top: 16px; }
  .inside .band-bottom { bottom: 0; height: 88px; }
  .inside .band-bottom .rule-inset { top: 8px; }
  .inside .rule-bottom { bottom: 104px; }
  .inside .flourish {
    position: absolute; left: 0; top: 200px; width: 160px; height: 310px;
    border-radius: 10% 60% 40% 10%;
    background: radial-gradient(ellipse at 35% 50%, var(--wine) 0%, var(--wine-soft) 55%, rgba(194,67,74,0) 100%);
  }
  .message {
    position: absolute; left: 560px; top: 206px; width: 370px;
    text-align: center; color: var(--wine); font-size: 16px; line-height: 25px;
  }
  .message .lead { font-size: 22px; }
  .message p + p { margin-top: 20px; }
  .message .signature {
    margin-top: 14px; font-family: "Kalam", cursive; font-weight: 300; font-size: 22px;
  }
  .rsvp {
    position: absolute; left: 600px; bottom: 20px; width: 330px;
    color: var(--paper); font-size: 15px; line-height: 23px;
  }
</style>
</head>
<body>

  <section class="card cover" aria-label="Vorderseite">
    <div class="band band-top"></div>
    <div class="rule rule-top"></div>
    <div class="flourish" role="img" aria-label="Florales Rankenornament in Weinrot und Zartrosa"></div>
    <h1 class="title">Einladung</h1>
    <div class="rule rule-bottom"></div>
    <div class="band band-bottom"><div class="rule-inset"></div></div>
  </section>

  <section class="card inside" aria-label="Innenseite">
    <div class="band band-top"></div>
    <div class="rule rule-top"></div>
    <div class="flourish" role="img" aria-label="Florales Rankenornament in Weinrot"></div>
    <div class="message">
      <p>Zu meinem <span class="lead">50. Geburtstag</span> möchte<br>ich Euch ganz herzlich einladen.</p>
      <p>Gefeiert wird am Samstag, den <span class="lead">10. Mai 2008</span><br>um 19.30 Uhr in der Gaststätte Muster in Musterhausen.</p>
      <p class="signature">Maria Muster</p>
    </div>
    <div class="rule rule-bottom"></div>
    <div class="band band-bottom"><div class="rule-inset"></div></div>
    <p class="rsvp">Wer verhindert sein sollte, melde sich bitte bis<br>zum 30. April unter&nbsp; (0 98 76) 54 32 bei mir ab.</p>
  </section>

</body>
</html>
```